Talent Management Company Needs Business Cards

Using one of the logos provided (attached) K&K Talent Collective needs a business card designed.
Please visit our website for more information about us-

www.kktalentcollective.net

The face should feature a dramatic presentation of the logo with the back being reserved for our professional information which is:

The information should be:
Darnell T. Fosbury
C.E.O
Email: dtfosbury@kktalentcollective.net
Mobile: 216-555-0193
Website: www.kktalentcollective.net

Marcus L. Fosbury
Director of Public Relations
Email: mlfosbury@kktalentcollective.net
Mobile: 216-555-0147

Rory J. Whitcomb
Director of Client Development
Email: rwhitcomb@kktalentcollective.net

Glenn Strauss
Director of Brand Development
Email: gstrauss@kktalentcollective.net

Would like the logo to have color. I would like to see one side red or black and the other side white but if it looks better in either black or red that would be fine to but would like to see how it comes out.

Please feel free to message me and if you would like just the icon alone I have other image files that I can send as well.

Target Market(s)

Professional Athletes, coaches, entertainers age 18-35 but also must be accepted in the business community

Industry/Entity Type

Business

Requirements
Must have
• 1) Use the logo
2) Double sided
3) Distinctive
Nice to have
• Small simple images for telephone, e-mail, and Url.

```html
<!DOCTYPE html>
<html lang="en">
<head>
<meta charset="utf-8">
<title>K&amp;K Talent Collective — Business Card</title>
<link href="https://fonts.googleapis.com/css2?family=Jura:wght@300;400&family=Michroma&display=swap" rel="stylesheet">
<style>
  :root {
    --bg: #9a9a9a;
    --red: #d8262b;
    --red-dark: #8f1116;
    --red-mid: #b8171d;
    --paper: #f2f2f0;
    --ink: #1e1e1e;
    --rule: #6c6c6c;
    --black: #1a1a1a;
    --white: #ffffff;
  }
  * { box-sizing: border-box; margin: 0; padding: 0; }
  html, body { width: 1200px; height: 720px; overflow: hidden; }
  body {
    background: var(--bg);
    display: flex;
    align-items: center;
    justify-content: center;
    gap: 40px;
    font-family: "Jura", sans-serif;
  }
  .card {
    position: relative;
    width: 540px;
    height: 310px;
    overflow: hidden;
    box-shadow: 0 6px 18px rgba(0,0,0,0.25);
  }

  /* Front */
  .card--front {
    background: radial-gradient(ellipse at 30% 20%, var(--red) 0%, var(--red-mid) 55%, var(--red-dark) 100%);
  }
  .front-glow {
    position: absolute;
    right: -60px;
    bottom: -80px;
    width: 320px;
    height: 320px;
    border-radius: 50%;
    background: radial-gradient(circle, rgba(0,0,0,0.18) 0%, rgba(0,0,0,0) 70%);
  }
  .front-brand {
    position: absolute;
    left: 44px;
    top: 118px;
    display: flex;
    align-items: center;
    gap: 14px;
  }
  .brand-mark {
    width: 34px;
    height: 34px;
    background: var(--white);
  }
  .brand-name {
    font-family: "Michroma", sans-serif;
    font-size: 21px;
    letter-spacing: 1px;
    color: var(--white);
    text-transform: uppercase;
  }

  /* Back */
  .card--back { background: var(--paper); }
  .name-band {
    position: absolute;
    left: 0;
    top: 34px;
    width: 462px;
    height: 40px;
    background: linear-gradient(90deg, var(--red) 0%, var(--red-mid) 60%, var(--red-dark) 100%);
    display: flex;
    align-items: center;
    padding-left: 30px;
    color: var(--white);
    font-weight: 300;
  }
  .name-band::before {
    content: "";
    position: absolute;
    left: 0; right: -78px;
    top: -5px;
    height: 1px;
    background: var(--red);
  }
  .name-band::after {
    content: "";
    position: absolute;
    left: 0; right: -78px;
    bottom: -5px;
    height: 1px;
    background: var(--red);
  }
  .person-name { font-size: 18px; letter-spacing: 0.5px; }
  .name-divider {
    width: 1px; height: 22px;
    background: rgba(255,255,255,0.7);
    margin: 0 14px;
  }
  .person-title { font-size: 13px; letter-spacing: 3px; }
  .corner-square {
    position: absolute;
    right: 0;
    top: 34px;
    width: 70px;
    height: 66px;
    background: linear-gradient(135deg, #3a3a3a, var(--black));
  }
  .back-brand {
    position: absolute;
    left: 30px;
    top: 140px;
    width: 170px;
    display: flex;
    align-items: center;
    gap: 10px;
  }
  .back-brand .brand-mark { width: 18px; height: 18px; background: var(--red); flex: none; }
  .back-brand .brand-name { color: var(--red); font-size: 13px; line-height: 1.5; letter-spacing: 0.5px; }
  .vertical-rule {
    position: absolute;
    left: 224px;
    top: 118px;
    width: 2px;
    height: 150px;
    background: var(--rule);
  }
  .contact-list {
    position: absolute;
    left: 244px;
    top: 178px;
    list-style: none;
    font-family: "Michroma", sans-serif;
    color: var(--ink);
  }
  .contact-list li {
    display: flex;
    align-items: center;
    gap: 10px;
    font-size: 11.5px;
    height: 22px;
  }
  .contact-list .phone { font-size: 15px; }
  .contact-icon { width: 12px; height: 12px; flex: none; }
</style>
</head>
<body>
  <section class="card card--front" aria-label="Card front">
    <div class="front-glow"></div>
    <div class="front-brand">
      <span class="brand-mark"></span>
      <span class="brand-name">K&amp;K Talent Collective</span>
    </div>
  </section>

  <section class="card card--back" aria-label="Card back">
    <div class="name-band">
      <span class="person-name">Darnell T. Fosbury</span>
      <span class="name-divider"></span>
      <span class="person-title">C.E.O</span>
    </div>
    <div class="corner-square"></div>

    <div class="back-brand">
      <span class="brand-mark"></span>
      <span class="brand-name">K&amp;K Talent Collective</span>
    </div>
    <div class="vertical-rule"></div>

    <ul class="contact-list">
      <li class="phone">
        <svg class="contact-icon" viewBox="0 0 12 12" aria-hidden="true"><rect x="3" y="0.5" width="6" height="11" rx="1.5" fill="none" stroke="#1e1e1e" stroke-width="1.2"/><circle cx="6" cy="9.3" r="0.8" fill="#1e1e1e"/></svg>
        216-555-0193
      </li>
      <li>
        <svg class="contact-icon" viewBox="0 0 12 12" aria-hidden="true"><rect x="0.5" y="2" width="11" height="8" rx="1" fill="#1e1e1e"/><path d="M1 2.5 L6 6.5 L11 2.5" fill="none" stroke="#f2f2f0" stroke-width="1"/></svg>
        dtfosbury@kktalentcollective.net
      </li>
      <li>
        <svg class="contact-icon" viewBox="0 0 12 12" aria-hidden="true"><circle cx="6" cy="6" r="5.5" fill="#1e1e1e"/><ellipse cx="6" cy="6" rx="2.2" ry="5" fill="none" stroke="#f2f2f0" stroke-width="0.8"/><path d="M1 6 H11" stroke="#f2f2f0" stroke-width="0.8"/></svg>
        www.kktalentcollective.net
      </li>
    </ul>
  </section>
</body>
</html>
```